Biz card, letterhead, envelopes for massage business
Massage Business for people and for Equine (horses)
Biz card, letterhead, envelopes for massage business - Massage Therapy
Use same font as used in my logo
simular to my logo
Modern
Marla Kessin
Certified Massage Therapist
P.O. Box 871, Fernhollow, OR 95718
marlakessin@quillpost.net
I provide massage for people and for horses. We need to creatively put the information on the back of the card. Of course we don't want to say "Human"..... when refering to horse we call it Equine Massage.
Human Massage Therapy.....Swedish, Deep Tissue, Relaxation, Hot Stone, On-Site Chair Massage Equine Massage Therapy...... Stridolan Certified Pellridge Method Relieves muscle pain, enhances performance, reduces inflamation, enhances muscle tone, increases endorphines - a horses natural pain killers For both : Relax Relieve Rejuvenate

```html
<!DOCTYPE html>
<html lang="en">
<head>
<meta charset="utf-8">
<title>Whole Stride Balance – Business Card</title>
<link rel="stylesheet" href="https://fonts.googleapis.com/css2?family=Questrial&display=swap">
<style>
  :root {
    --stage: #e9e6df;
    --leaf: #7ba428;
    --leaf-dark: #6a9220;
    --bark: #6b3a1c;
    --paper: #ffffff;
    --paper-shade: #eeeeee;
    --ink: #555555;
  }
  html, body {
    margin: 0;
    padding: 0;
    width: 1200px;
    height: 904px;
    overflow: hidden;
    background: var(--stage);
    font-family: "Questrial", "Century Gothic", sans-serif;
  }
  .canvas {
    position: relative;
    width: 1200px;
    height: 904px;
  }
  .card {
    position: absolute;
    width: 540px;
    height: 310px;
    border-radius: 22px;
    overflow: hidden;
    box-shadow: 0 10px 24px rgba(0,0,0,0.22);
  }
  /* Back of card */
  .card-back {
    left: 110px;
    top: 90px;
    background: var(--leaf);
  }
  .card-back .mark {
    position: absolute;
    left: 36px;
    top: 140px;
    display: flex;
    align-items: center;
    gap: 8px;
    color: var(--paper);
    font-size: 15px;
  }
  .card-back .mark .dot {
    width: 14px;
    height: 14px;
    border: 2px solid var(--paper);
    border-radius: 50%;
  }
  .services {
    position: absolute;
    left: 210px;
    top: 26px;
    width: 290px;
    text-align: center;
    color: var(--paper);
    font-size: 11.5px;
    line-height: 1.38;
  }
  .services p { margin: 0 0 8px; }
  .services .tagline { margin-top: 6px; }
  /* Front of card */
  .card-front {
    left: 560px;
    top: 500px;
    background: linear-gradient(180deg, var(--paper) 0%, var(--paper-shade) 100%);
  }
  .card-front .waves {
    position: absolute;
    left: 0;
    bottom: 0;
    width: 540px;
    height: 130px;
  }
  .brand {
    position: absolute;
    left: 34px;
    top: 108px;
    display: flex;
    align-items: center;
    gap: 10px;
    color: var(--bark);
    font-size: 25px;
  }
  .brand .dot {
    width: 18px;
    height: 18px;
    border: 2px solid var(--leaf);
    border-radius: 50%;
  }
  .contact {
    position: absolute;
    left: 340px;
    top: 36px;
    color: var(--ink);
    font-size: 12.5px;
    line-height: 1.4;
  }
  .contact .name {
    color: var(--leaf);
    font-size: 17px;
    margin: 0;
  }
  .contact .role { margin: 0 0 14px; }
  .contact .address { margin: 0 0 12px; }
  .contact .line {
    display: flex;
    align-items: center;
    gap: 8px;
    margin: 0 0 3px;
  }
  .contact svg { width: 13px; height: 13px; flex: none; }
</style>
</head>
<body>
<main class="canvas">

  <section class="card card-back" aria-label="Card back">
    <div class="mark"><span class="dot"></span><span>Whole Stride Balance</span></div>
    <div class="services">
      <p>Human Massage Therapy<br>Swedish<br>Deep Tissue<br>Relaxation<br>Hot Stone<br>On-Site Chair Massage</p>
      <p>Equine Massage Therapy<br>Stridolan Certified<br>Pellridge Method</p>
      <p>Relieves<br>muscle pain<br>enhances performance<br>reduces inflammation<br>enhances muscle tone<br>increases endorphins - a horses natural pain killers</p>
      <p class="tagline">For both : &nbsp;Relax Relieve Rejuvenate</p>
    </div>
  </section>

  <section class="card card-front" aria-label="Card front">
    <svg class="waves" viewBox="0 0 540 130" preserveAspectRatio="none" aria-hidden="true">
      <path d="M0 95 C150 45 330 20 540 22 L540 34 C340 34 170 62 0 112 Z" fill="var(--bark)"/>
      <path d="M0 110 C170 62 340 40 540 40 L540 130 L0 130 Z" fill="var(--paper)"/>
      <path d="M0 112 C180 78 360 62 540 58 L540 130 L0 130 Z" fill="var(--leaf)"/>
    </svg>

    <div class="brand"><span class="dot"></span><span>Whole Stride Balance</span></div>

    <div class="contact">
      <p class="name">Marla Kessin</p>
      <p class="role">Certified Massage Therapist</p>
      <p class="address">P.O. Box 871, Fernhollow<br>OR 95718</p>
      <p class="line">
        <svg viewBox="0 0 12 12" aria-hidden="true"><rect x="3" y="0.5" width="6" height="11" rx="1.2" fill="none" stroke="var(--ink)" stroke-width="1.2"/><circle cx="6" cy="9.5" r="0.7" fill="var(--ink)"/></svg>
        <span>555.210.0147</span>
      </p>
      <p class="line">
        <svg viewBox="0 0 12 12" aria-hidden="true"><rect x="0.5" y="2.5" width="11" height="7" fill="var(--bark)"/><path d="M0.5 2.5 L6 6.5 L11.5 2.5" fill="none" stroke="var(--paper)" stroke-width="0.9"/></svg>
        <span>marlakessin@quillpost.net</span>
      </p>
    </div>
  </section>

</main>
</body>
</html>
```